Veltrano - Mechanic/Collision Center Business Card

We're looking for a business card design for our mechanic/ collision repair shop.

Can be with colours or monochromatic.

See the attached files.

Many thanks

```html
<!DOCTYPE html>
<html lang="en">
<head>
<meta charset="utf-8">
<title>Veltrano – Business Card</title>
<link href="https://fonts.googleapis.com/css2?family=Arimo:wght@400;700&display=swap" rel="stylesheet">
<style>
  :root {
    --page-bg: #e9ebee;
    --card-blue: #45b3e6;
    --card-edge: #2f9bd0;
    --ink: #111418;
    --ink-soft: #1d2a33;
    --bar-grey: #7d8287;
    --bar-border: #3a3f44;
    --bar-text: #4fb8ea;
    --ghost: rgba(20, 60, 90, 0.12);
  }
  * { box-sizing: border-box; margin: 0; padding: 0; }
  html, body {
    width: 1200px; height: 835px; overflow: hidden;
    background: var(--page-bg);
    font-family: "Arimo", Arial, sans-serif;
  }
  .sheet {
    position: relative; width: 1200px; height: 835px;
    display: flex; flex-direction: column; align-items: center; justify-content: center; gap: 50px;
  }
  .card {
    position: relative; width: 620px; height: 330px;
    background: var(--card-blue);
    border-radius: 22px;
    box-shadow: 0 6px 0 var(--card-edge), 0 12px 24px rgba(0,0,0,0.18);
    overflow: hidden;
  }
  /* front */
  .card-front { display: flex; align-items: center; padding: 0 40px; }
  .brand {
    display: flex; align-items: center; gap: 12px;
    width: 270px;
  }
  .brand-dot {
    width: 34px; height: 34px; border-radius: 50%;
    background: var(--ink);
    flex: none;
  }
  .brand-name {
    font-weight: 700; font-size: 40px; letter-spacing: 1px;
    color: var(--ink);
  }
  .details { margin-left: 40px; color: var(--ink); }
  .company { font-size: 22px; font-weight: 700; }
  .role { font-size: 14px; font-weight: 700; margin-bottom: 20px; letter-spacing: 0.5px; }
  .contact-list { list-style: none; }
  .contact-list li {
    display: flex; align-items: center; gap: 10px;
    font-size: 16px; line-height: 1.7;
  }
  .contact-list li.address { font-size: 19px; }
  .icon { width: 16px; height: 16px; flex: none; }
  /* back */
  .card-back { display: flex; flex-direction: column; align-items: center; }
  .ghost-name {
    position: absolute; left: 50%; top: 88px; transform: translateX(-50%);
    font-weight: 700; font-size: 96px; letter-spacing: 3px;
    color: var(--ghost); white-space: nowrap;
  }
  .back-brand { position: relative; margin-top: 112px; width: auto; }
  .back-brand .brand-name { font-size: 44px; }
  .info-bar {
    position: absolute; left: 24px; right: 24px; bottom: 30px; height: 54px;
    background: var(--bar-grey);
    border: 5px solid var(--bar-border);
    border-radius: 27px;
    display: flex; align-items: center; gap: 18px; padding: 0 28px;
    color: var(--bar-text);
  }
  .bar-name { font-weight: 700; font-size: 24px; letter-spacing: 1px; }
  .bar-role { font-size: 18px; letter-spacing: 1px; }
  .bar-phone { margin-left: auto; display: flex; align-items: center; gap: 8px; font-size: 18px; }
</style>
</head>
<body>
<main class="sheet">

  <section class="card card-front">
    <div class="brand">
      <span class="brand-dot"></span>
      <span class="brand-name">VELTRANO</span>
    </div>
    <div class="details">
      <p class="company">Veltrano, LDA</p>
      <p class="role">founder &amp; CEO</p>
      <ul class="contact-list">
        <li class="address">
          <svg class="icon" viewBox="0 0 16 16"><path d="M8 1a5 5 0 0 0-5 5c0 4 5 9 5 9s5-5 5-9a5 5 0 0 0-5-5zm0 7a2 2 0 1 1 0-4 2 2 0 0 1 0 4z" fill="#111418"/></svg>
          Rua do Ferreiro, 42
        </li>
        <li>
          <svg class="icon" viewBox="0 0 16 16"><circle cx="8" cy="8" r="7" fill="none" stroke="#111418" stroke-width="2"/><rect x="4" y="6" width="8" height="4" fill="#111418"/></svg>
          1900-118 Lisboa
        </li>
        <li>
          <svg class="icon" viewBox="0 0 16 16"><circle cx="8" cy="8" r="8" fill="#111418"/><path d="M6 4c-1 1-1 3 1 5s4 2 5 1l-1.5-1.5-1 .7-2.7-2.7.7-1z" fill="#45b3e6"/></svg>
          +351210004172
        </li>
        <li>
          <svg class="icon" viewBox="0 0 16 16"><circle cx="8" cy="8" r="8" fill="#111418"/><rect x="4" y="5" width="8" height="6" fill="#45b3e6"/><path d="M4 5l4 3 4-3" fill="none" stroke="#111418" stroke-width="1"/></svg>
          veltrano.mail@example.com
        </li>
        <li>
          <svg class="icon" viewBox="0 0 16 16"><circle cx="8" cy="8" r="8" fill="#111418"/></svg>
          www.veltrano-auto.pt
        </li>
      </ul>
    </div>
  </section>

  <section class="card card-back">
    <span class="ghost-name" aria-hidden="true">VELTRANO</span>
    <div class="brand back-brand">
      <span class="brand-dot"></span>
      <span class="brand-name">VELTRANO</span>
    </div>
    <div class="info-bar">
      <span class="bar-name">Rui Matos:</span>
      <span class="bar-role">info of manager</span>
      <span class="bar-phone">
        <svg class="icon" viewBox="0 0 16 16"><circle cx="8" cy="8" r="8" fill="#4fb8ea"/><path d="M6 4c-1 1-1 3 1 5s4 2 5 1l-1.5-1.5-1 .7-2.7-2.7.7-1z" fill="#7d8287"/></svg>
        +351912005841
      </span>
    </div>
  </section>

</main>
</body>
</html>
```